Job advertisement

A graphic job advertisement. It's supposed to be slightly different from the normal ads. Eye-catcher and later the text for the job description.

```html
<!DOCTYPE html>
<html lang="de">
<head>
<meta charset="utf-8">
<title>Stellenanzeige – Power-Worker</title>
<link href="https://fonts.googleapis.com/css2?family=Roboto+Condensed:wght@300;400;500;700&display=swap" rel="stylesheet">
<style>
  :root {
    --backdrop: #d2d2d2;
    --navy-deep: #050a18;
    --navy: #1c2a48;
    --glow: #a9b8d2;
    --red: #e8333a;
    --slate: #8a9aa2;
    --text-dark: #1d1d1d;
    --white: #ffffff;
  }
  * { box-sizing: border-box; margin: 0; padding: 0; }
  html, body {
    width: 1011px; height: 1200px; overflow: hidden;
    background: var(--backdrop);
    font-family: "Roboto Condensed", Arial, sans-serif;
  }
  .ad {
    position: absolute; left: 117px; top: 94px;
    width: 777px; height: 973px;
    background: var(--white);
    box-shadow: 0 4px 14px rgba(0,0,0,.3);
    overflow: hidden;
  }
  .hero-visual {
    position: absolute; left: 0; top: 0; width: 777px; height: 790px;
    background:
      radial-gradient(ellipse 210px 300px at 390px 380px, #dfe6f2 0%, #8797b6 30%, rgba(60,78,112,.6) 60%, transparent 100%),
      radial-gradient(ellipse 360px 220px at 330px 650px, rgba(150,160,190,.55) 0%, transparent 80%),
      linear-gradient(180deg, var(--navy-deep) 0%, var(--navy) 40%, #17213a 75%, var(--navy-deep) 100%);
  }
  .term {
    position: absolute;
    color: var(--white);
    font-weight: 700; font-size: 25px; letter-spacing: .3px;
    text-shadow: 0 1px 3px rgba(0,0,0,.6);
    line-height: 1;
  }
  .headline-band {
    position: absolute; left: 40px; top: 762px; width: 400px; height: 84px;
  }
  .headline-band svg { position: absolute; left: 0; top: 0; }
  .headline-intro {
    position: absolute; left: 22px; top: 10px;
    color: var(--white); font-weight: 300; font-size: 27px; line-height: 1;
  }
  .headline-title {
    position: absolute; left: 21px; top: 40px;
    color: var(--white); font-weight: 700; font-size: 41px; line-height: 1;
    letter-spacing: .5px;
  }
  .apply {
    position: absolute; left: 50px; top: 882px;
  }
  .apply-label { font-size: 20px; color: var(--text-dark); font-weight: 400; }
  .apply-mail {
    display: flex; align-items: center; gap: 8px;
    margin-left: -4px; margin-top: 2px;
    color: var(--red); font-weight: 500; font-size: 23px;
  }
  .brand {
    position: absolute; left: 457px; top: 870px;
    display: flex; align-items: center; gap: 14px;
  }
  .brand-dot {
    width: 44px; height: 44px; border-radius: 50%; background: var(--red);
  }
  .brand-name {
    color: var(--slate); font-weight: 400; line-height: .95;
  }
  .brand-name .small { display: block; font-size: 22px; margin-left: 58px; }
  .brand-name .large { display: block; font-size: 38px; }
</style>
</head>
<body>
  <article class="ad">
    <div class="hero-visual" role="img" aria-label="Photo: a glowing wireframe light bulb made of connected network points floating above an open hand, on a dark blue network background"></div>

    <span class="term" style="left:127px; top:164px;">STORM</span>
    <span class="term" style="left:156px; top:231px;">VOLT</span>
    <span class="term" style="left:194px; top:300px;">WATT</span>
    <span class="term" style="left:551px; top:180px;">AMPERE</span>
    <span class="term" style="left:519px; top:282px;">OHM</span>
    <span class="term" style="left:497px; top:360px;">SPANNUNG</span>
    <span class="term" style="left:343px; top:515px;">LEISTUNG</span>

    <div class="headline-band">
      <svg width="400" height="84" viewBox="0 0 400 84" aria-hidden="true">
        <polygon points="0,0 328,0 353,84 0,84" fill="var(--red)"/>
        <polygon points="337,0 347,0 373,84 362,84" fill="var(--slate)"/>
      </svg>
      <p class="headline-intro">Wir suchen SIE !</p>
      <h1 class="headline-title">POWER-WORKER</h1>
    </div>

    <div class="apply">
      <p class="apply-label">Bewerbung an</p>
      <p class="apply-mail">
        <svg width="17" height="13" viewBox="0 0 17 13" aria-hidden="true">
          <rect x="0" y="0" width="17" height="13" rx="1.5" fill="var(--red)"/>
          <polyline points="1,1.5 8.5,7.5 16,1.5" fill="none" stroke="var(--white)" stroke-width="1.6"/>
        </svg>
        jobs@elektro-brandt.de
      </p>
    </div>

    <div class="brand">
      <span class="brand-dot" aria-hidden="true"></span>
      <p class="brand-name"><span class="small">elektro</span><span class="large">brandt</span></p>
    </div>
  </article>
</body>
</html>
```